Tri-fold Brochure Design for Banking Business

The brochure we have needs to be improved - more business like and more attractive. Logo file and brochure is attached. I would like to be able to edit the text after you get done. Your ideas and changes to text are welcome. See our website www.korvanbridgegrp.com for our theme. We can use indesign to edit the text after you complete. However, please make changes to the text we have in the design that it uploaded. Your comments and changes are welcome.

Target Market(s)

Human Resources and learning & development staff at the global investment banks - Pellham Trask, QWNR, etc.

Industry/Entity Type

Investment Banking

Logo Text

Korvan Bridge Group

Font styles to use
Serif
Sans Serif

Colors
33a6d7
0493ce
3277b5
fbf289
fdf9cf
fbee3e
0555a3
85acd3

Requirements
Must have
• Must be similar to our website www.korvanbridgegrp.com. Needs to be business-like, clean fonts, sharp design. Our logo - of course.
Nice to have
• City images - seems to be our theme.

```html
<!DOCTYPE html>
<html lang="en">
<head>
<meta charset="utf-8">
<title>Korvan Bridge Group – Tri-fold Brochure</title>
<link href="https://fonts.googleapis.com/css2?family=Questrial&family=Montserrat:wght@600;700&display=swap" rel="stylesheet">
<style>
:root{
  --stage:#2e2e2e;
  --ink:#3a3a3a;
  --heading:#1a1a1a;
  --rule:#0555a3;
  --sky:#a9c6e6;
  --sky-deep:#85acd3;
  --navy:#2f4a78;
  --navy-deep:#1d2f52;
  --tab:#0555a3;
  --white:#ffffff;
  --tick:#fbee3e;
}
*{box-sizing:border-box;margin:0;padding:0}
html,body{width:814px;height:1200px;overflow:hidden}
body{background:var(--stage);font-family:"Questrial",sans-serif;color:var(--ink);position:relative}
.sheet{position:absolute;left:66px;width:683px;height:527px;overflow:hidden;background:var(--white)}
.sheet--outside{top:58px}
.sheet--inside{top:614px}
.block{position:absolute}
.photo{position:absolute}
.copy{font-size:10.4px;line-height:12.4px}
.copy p{margin-bottom:7px}
.heading{font-family:"Montserrat",sans-serif;font-weight:700;font-size:18px;color:var(--heading);letter-spacing:.3px}
.heading-rule{position:absolute;height:1px;background:var(--rule)}
.heading-rule::before{content:"";position:absolute;left:12px;top:0;border:5px solid transparent;border-top-color:var(--rule);border-bottom:0}

/* outside */
.about{left:0;top:0;width:228px;height:219px;background:linear-gradient(90deg,#fff 40%,#d9d9d9)}
.about .heading{position:absolute;left:19px;top:16px}
.about .heading-rule{left:0;top:41px;width:228px}
.about .copy{position:absolute;left:19px;top:50px;width:200px}
.contacts{left:228px;top:0;width:228px;height:118px;background:var(--sky);text-align:center;font-size:8.8px;line-height:11.6px;color:#1d3560;padding-top:17px}
.contacts b{font-family:"Montserrat",sans-serif;font-weight:600;font-size:8px;display:block}
.brand-panel{left:456px;top:0;width:227px;height:118px;background:var(--sky);display:flex;align-items:center;justify-content:center;gap:8px}
.brand-mark{width:14px;height:14px;background:var(--navy-deep)}
.brand-name{font-size:17px;color:var(--navy-deep);letter-spacing:.5px}
.space-panel{left:228px;top:397px;width:228px;height:130px}
.space-panel .web{position:absolute;top:16px;width:100%;text-align:center;color:#fff;font-family:"Montserrat",sans-serif;font-weight:600;font-size:10px}
.space-panel .service{position:absolute;top:89px;width:100%;text-align:center;color:#fff;font-family:"Montserrat",sans-serif;font-weight:600;font-size:10px}
.tagline{left:456px;top:397px;width:227px;height:130px;background:var(--navy);display:flex;align-items:center;justify-content:center;text-align:center;color:#fff;font-family:"Montserrat",sans-serif;font-weight:700;font-size:17px;line-height:22px}

/* inside */
.why{left:18px;top:32px;width:191px;height:286px;background:rgba(20,28,45,.88);color:#fff;padding:42px 12px 0 16px}
.why-tab{left:36px;top:19px;width:156px;height:29px;background:var(--tab);color:#fff;font-family:"Montserrat",sans-serif;font-weight:700;font-size:14.5px;display:flex;align-items:center;justify-content:center;letter-spacing:.4px}
.why .copy{text-align:justify}
.why ul{list-style:none;font-size:10.4px;line-height:12.4px}
.why li{position:relative;padding-left:12px;margin-bottom:7px}
.why li svg{position:absolute;left:0;top:2px}
.services{left:228px;top:0;width:228px;height:326px;background:linear-gradient(90deg,#fff 50%,#e4e4e4)}
.team{left:456px;top:0;width:227px;height:326px;background:linear-gradient(90deg,#fff 50%,#e4e4e4)}
.services .heading,.team .heading{position:absolute;left:18px;top:16px}
.services .heading-rule,.team .heading-rule{left:0;top:40px;width:100%}
.services .copy{position:absolute;left:18px;top:49px;width:200px}
.team .copy{position:absolute;left:18px;top:49px;width:196px}
.team .copy.after{top:271px}
.contact-panel{left:456px;top:326px;width:227px;height:201px}
.contact-panel .ask{position:absolute;top:92px;width:100%;text-align:center;color:#f1f4f8;font-size:11px}
.contact-panel .cta{position:absolute;top:107px;width:100%;text-align:center;color:#fff;font-family:"Montserrat",sans-serif;font-weight:700;font-size:12.5px}
</style>
</head>
<body>

<section class="sheet sheet--outside">
  <div class="block about">
    <h2 class="heading">ABOUT US</h2>
    <div class="heading-rule"></div>
    <div class="copy">
      <p>Korvan Bridge Group efficiently provides complete sales, marketing and logistical support for all our programs, no matter the location.</p>
      <p>Our globally located trainers have extensive experience, both as industry professionals and as trainers.</p>
      <p>Our highly qualified logistical team complement the training services, providing reliable and efficient support.</p>
    </div>
  </div>
  <div class="photo" role="img" aria-label="City skyline of high-rise towers at dusk" style="left:0;top:219px;width:228px;height:308px;background:linear-gradient(160deg,#9a98a6 0%,#4d5566 40%,#2a3340 75%,#3a3026 100%)"></div>

  <div class="block contacts">
    <b>GLOBAL:</b>elena.marchi@korvanbridgegrp.com
    <b>ASIA:</b>paul.wexley@korvanbridgegrp.com
    <b>UNITED STATES:</b>sam.ortega@korvanbridgegrp.com
    <b>EUROPE:</b>neil.carver@korvanbridgegrp.com
  </div>
  <div class="block brand-panel">
    <span class="brand-mark"></span>
    <span class="brand-name">Korvan Bridge Group</span>
  </div>

  <div class="photo" role="img" aria-label="Looking up at glass skyscrapers lit at night in teal tones" style="left:228px;top:118px;width:455px;height:279px;background:linear-gradient(135deg,#6f8a9a 0%,#1f4a55 35%,#0f3a3c 60%,#3f7f80 100%)"></div>

  <div class="block space-panel">
    <div class="photo" role="img" aria-label="Earth seen from space with city lights at night" style="inset:0;background:radial-gradient(ellipse at 50% 95%,#3a78b8 0%,#123058 35%,#060d1f 75%)"></div>
    <div class="web">www.korvanbridgegrp.com</div>
    <div class="service">Worldwide Training Service</div>
  </div>
  <div class="block tagline">Your Expert Training<br>and<br>Consulting Partner</div>
</section>

<section class="sheet sheet--inside">
  <div class="photo" role="img" aria-label="Aerial view of dense city blocks in cool blue tones" style="left:0;top:0;width:228px;height:527px;background:linear-gradient(180deg,#8ea4c4 0%,#a9b7cc 45%,#6d7f9c 75%,#2f3d57 100%)"></div>
  <div class="block why">
    <div class="copy">
      <p>Korvan Bridge Group is dedicated to providing you and your firm with the highest level of service.</p>
      <p>We provide dedicated sales and logistics support for each program to insure consistent, reliable results.</p>
    </div>
    <ul>
      <li><svg width="8" height="8" viewBox="0 0 8 8"><rect x=".5" y="1.5" width="6" height="6" fill="none" stroke="var(--tick)"/><path d="M1.8 4.2l1.6 1.6L7.5.5" fill="none" stroke="var(--tick)" stroke-width="1.2"/></svg>Highly qualified, international pool of trainers</li>
      <li><svg width="8" height="8" viewBox="0 0 8 8"><rect x=".5" y="1.5" width="6" height="6" fill="none" stroke="var(--tick)"/><path d="M1.8 4.2l1.6 1.6L7.5.5" fill="none" stroke="var(--tick)" stroke-width="1.2"/></svg>Strong client relationship management and support</li>
      <li><svg width="8" height="8" viewBox="0 0 8 8"><rect x=".5" y="1.5" width="6" height="6" fill="none" stroke="var(--tick)"/><path d="M1.8 4.2l1.6 1.6L7.5.5" fill="none" stroke="var(--tick)" stroke-width="1.2"/></svg>Competitive pricing and flexibility</li>
      <li><svg width="8" height="8" viewBox="0 0 8 8"><rect x=".5" y="1.5" width="6" height="6" fill="none" stroke="var(--tick)"/><path d="M1.8 4.2l1.6 1.6L7.5.5" fill="none" stroke="var(--tick)" stroke-width="1.2"/></svg>Outcome driven approach directly matches your company's needs</li>
    </ul>
  </div>
  <div class="block why-tab">WHY CHOOSE US?</div>

  <div class="block services">
    <h2 class="heading">OUR SERVICES</h2>
    <div class="heading-rule"></div>
    <div class="copy">
      <p>Korvan Bridge Group provides best in class services for all our clients.</p>
      <p>We provide highly customized programs tailored to your specific requirements.</p>
      <p>Direct interaction between our clients, consulting trainers and client service staff ensures measurable outcomes for program participants.</p>
      <p>We facilitate learning outcomes using a blended methodology combining interactive analysis, hands-on experiential models, market simulations and a state-of-the-art learning management system.</p>
      <p>Our material databanks are continuously updated to insure accuracy and effectiveness of our services.</p>
    </div>
  </div>
  <div class="photo" role="img" aria-label="Business professional touching a digital training interface with skill keywords" style="left:228px;top:326px;width:228px;height:201px;background:linear-gradient(135deg,#5d8fc2 0%,#3a6aa0 50%,#a7c3e0 100%)"></div>

  <div class="block team">
    <h2 class="heading">OUR TEAM</h2>
    <div class="heading-rule"></div>
    <div class="copy">Our Consulting Trainers are located globally and recognized by the industry as highly effective trainers and program facilitators.</div>
    <div class="photo" role="img" aria-label="Group of business people standing on top of a globe" style="left:19px;top:118px;width:190px;height:143px;background:linear-gradient(180deg,#b8cadc 0%,#8ea5bd 45%,#5c7a5a 75%,#3d5f8a 100%)"></div>
    <div class="copy after">Korvan provides global expertise for our programs with local talent for program facilitation.</div>
  </div>
  <div class="block contact-panel">
    <div class="photo" role="img" aria-label="Hand holding a phone over a faded city skyline" style="inset:0;background:linear-gradient(180deg,#7d8fa8 0%,#94a4ba 50%,#8393aa 100%)"></div>
    <div class="ask">Need more information?</div>
    <div class="cta">Contact us!</div>
  </div>
</section>

</body>
</html>
```